New nutrition counseling business needs a flyer and logo design for marketing purposes

Need a new flyer for distribution to advertise and inform the public about new Dietetic Counseling service. The new business name is Harbor of Vitality with “Harbor” being the main name. It will provide nutrition consultation services to individuals who seek to change their dietary habits to achieve a variety of different health objectives. These objectives can include, but are not limited to weight management, enhanced athletic performance, improved health biomarkers, and reducing the risks or symptoms of chronic nutrition related diseases. The services provided include direct one on one counseling that entails health and nutrition assessments, evaluation of goals, and the determination of strategies to meet these goals. We would like to see designs that use an ocean color scheme with purple aspects as well. Color and logo ideas attached in uploads. Please include logo on the flyer as well.

Target Market(s)

General Population

Colors
0094D4
00A9DD
6FCCEA
C7EBF8
E9F6FB
00AB8E
00BBA5
67D7C9
C6EFE9
E9F9F6
6B429C
8869AF
B7A5CE
E3DAEB
F3F0F8

Requirements
Nice to have
• Pictures of nourishing foods, fruits, vegetables etc.
Should not have
• Do not include people in flyer or logo design

```html
<!DOCTYPE html>
<html lang="en">
<head>
<meta charset="utf-8">
<title>Harbor of Vitality – Flyer</title>
<link rel="stylesheet" href="https://fonts.googleapis.com/css2?family=Raleway:ital,wght@0,400;0,500;0,600;0,700;0,800;1,400;1,700;1,800&family=Montserrat:wght@700;800&display=swap">
<style>
  :root{
    --teal:#3fb48f;
    --teal-soft:#8fd6bd;
    --navy:#1b3f8c;
    --navy-band:#17418b;
    --paper:#ffffff;
    --backdrop:#ececec;
    --photo-light:#f6f7f8;
    --photo-mid:#e6e9ec;
  }
  *{box-sizing:border-box;margin:0;padding:0}
  html,body{width:688px;height:1200px;overflow:hidden;background:var(--backdrop)}
  body{font-family:"Raleway",sans-serif;color:var(--navy)}
  .flyer{position:absolute;left:44px;top:0;width:600px;height:1200px;background:var(--paper);overflow:hidden}

  .brand{position:absolute;top:38px;left:0;width:100%;text-align:center;color:var(--teal);font-weight:700}
  .brand-line{display:block;line-height:1}
  .brand-name{font-size:84px;letter-spacing:1px}
  .brand-sub{font-size:30px;margin-top:8px}

  .hero-photo{position:absolute;left:40px;top:182px;width:520px;height:424px;
    background:linear-gradient(180deg,var(--photo-light) 0%,var(--photo-mid) 50%,var(--photo-light) 100%)}

  .tagline{position:absolute;top:628px;width:100%;text-align:center;font-size:37px;font-style:italic;font-weight:400;color:var(--navy);letter-spacing:-.3px}
  .tagline strong{font-weight:800;color:var(--teal)}

  .section-head{position:absolute;top:697px;left:56px;width:487px;height:35px}
  .section-head .rule{position:absolute;top:17px;left:0;width:100%;height:1px;background:var(--teal)}
  .section-head .pill{position:absolute;left:135px;width:218px;height:35px;border-radius:18px;background:var(--teal);color:#fff;font-weight:700;font-size:26px;text-align:center;line-height:35px;box-shadow:0 3px 5px rgba(0,0,0,.15)}

  .services{position:absolute;top:751px;list-style:none;font-size:18.5px;line-height:24px;color:var(--navy)}
  .services.col-left{left:65px;width:232px}
  .services.col-right{left:344px;width:214px}
  .services li{position:relative;margin-bottom:4px}
  .services li::before{content:"";position:absolute;left:-17px;top:8px;width:7px;height:7px;border-radius:50%;background:var(--navy);box-shadow:0 0 0 2.5px var(--teal)}

  .consult-note{position:absolute;top:1010px;left:40px;width:520px;height:66px}
  .consult-note .chat-icon{position:absolute;left:0;top:2px;width:50px;height:46px}
  .consult-note .modes{position:absolute;right:287px;top:0;width:185px;text-align:right;font-size:17px;font-weight:700;line-height:21px;color:var(--teal)}
  .consult-note .divider{position:absolute;left:247px;top:2px;width:1px;height:60px;background:#c9d4e6}
  .consult-note .offer{position:absolute;left:263px;top:0;width:262px;font-size:17px;line-height:21.5px;color:var(--navy)}
  .consult-note .offer b{font-weight:800}

  .contact-rule{position:absolute;top:1116px;left:0;width:100%;height:1px;background:var(--teal-soft)}
  .contact-band{position:absolute;top:1123px;left:0;width:100%;height:77px;background:var(--navy-band)}
  .phone-pill{position:absolute;top:1094px;left:133px;width:335px;height:46px;border-radius:23px;background:var(--teal);z-index:2}
  .phone-pill .icon{position:absolute;left:-1px;top:-2px;width:50px;height:50px;border-radius:50%;background:#fff;border:3px solid var(--teal)}
  .phone-pill .icon svg{position:absolute;left:1px;top:1px}
  .phone-pill .number{position:absolute;left:63px;top:0;font-family:"Montserrat",sans-serif;font-weight:800;font-size:31px;line-height:46px;color:#fff;letter-spacing:1px}
  .email{position:absolute;top:1150px;width:100%;text-align:center;color:#fff;font-size:26px;font-weight:400}
</style>
</head>
<body>
<main class="flyer">
  <header class="brand">
    <span class="brand-line brand-name">Harbor</span>
    <span class="brand-line brand-sub">of Vitality</span>
  </header>

  <div class="hero-photo" role="img" aria-label="Photo: bowl of fresh vegetables, fruit and nuts beside a stethoscope and glucose meter on a white table"></div>

  <h2 class="tagline">Where <strong>health</strong> meets <strong>care</strong></h2>

  <div class="section-head">
    <span class="rule"></span>
    <h3 class="pill">Our Services</h3>
  </div>

  <ul class="services col-left">
    <li>Medical Nutrition Therapy for chronic conditions such as diabetes, hypertension, high cholesterol</li>
    <li>Weight Management</li>
    <li>Healthy Eating and Meal Planning</li>
    <li>Nutrition for Athletic Performance</li>
  </ul>
  <ul class="services col-right">
    <li>Pre and Post Natal Nutrition</li>
    <li>Personalized meal plans uniquely catered to each individual</li>
    <li>Highly collaborative approach to help you meet your goals</li>
  </ul>

  <section class="consult-note">
    <svg class="chat-icon" viewBox="0 0 50 46" aria-hidden="true">
      <rect x="12" y="8" width="36" height="26" rx="4" fill="none" stroke="#3fb48f" stroke-width="2.5"/>
      <path d="M40 34 L42 42 L34 34" fill="none" stroke="#3fb48f" stroke-width="2.5" stroke-linejoin="round"/>
      <rect x="2" y="2" width="36" height="26" rx="4" fill="#fff" stroke="#1b3f8c" stroke-width="2.5"/>
      <path d="M10 28 L8 37 L18 28" fill="#fff" stroke="#1b3f8c" stroke-width="2.5" stroke-linejoin="round"/>
      <line x1="8" y1="10" x2="30" y2="10" stroke="#3fb48f" stroke-width="2.5"/>
      <line x1="8" y1="16" x2="30" y2="16" stroke="#3fb48f" stroke-width="2.5"/>
      <line x1="8" y1="22" x2="22" y2="22" stroke="#3fb48f" stroke-width="2.5"/>
    </svg>
    <p class="modes">Both in-person and virtual consultations are offered</p>
    <span class="divider"></span>
    <p class="offer"><b>Lets Chat! Free 15-minute introductory consultation</b> to discuss program details and rates</p>
  </section>

  <div class="contact-rule"></div>
  <div class="contact-band"></div>
  <div class="phone-pill">
    <span class="icon">
      <svg viewBox="0 0 42 42" width="42" height="42" aria-hidden="true">
        <path d="M14 11c1.5-1 3-.5 3.8 1l2 3.6c.6 1.2.2 2.4-.8 3.1l-1.3 1c.8 2.4 2.6 4.4 5 5.4l1.1-1.3c.8-1 2.1-1.2 3.2-.5l3.4 2.3c1.4 1 1.6 2.5.5 3.8l-1.7 1.8c-1.4 1.4-3.6 1.7-6 .7-5.6-2.3-9.8-7-11.4-12.7-.6-2.3-.1-4.4 1.5-5.6z" fill="#1b3f8c"/>
        <path d="M24 10a9 9 0 0 1 8 8M24 14.5a4.5 4.5 0 0 1 4 4" fill="none" stroke="#1b3f8c" stroke-width="2" stroke-linecap="round"/>
      </svg>
    </span>
    <span class="number">352-555-0148</span>
  </div>
  <p class="email">mail us: hello@harborvitality.net</p>
</main>
</body>
</html>
```